Flyer für Vertrieb und Montage von Photovoltaikanlagen
Zielgruppe
Vertrieb und Montage von Photovoltaikanlagen für jeden Hausbesitzer
Aufgabenstellung
auf unsere WEB Site kann der Kunde sich vorab die Gesamtkosten der Anlage ausrechnen
ohne Angabe seine Identität preiszugeben

```html
<!DOCTYPE html>
<html lang="de">
<head>
<meta charset="utf-8">
<title>Birkenhaintom – Flyer Photovoltaik</title>
<link href="https://fonts.googleapis.com/css2?family=Open+Sans:wght@400;600;700;800&display=swap" rel="stylesheet">
<style>
  :root {
    --brand-blue: #1f5fa8;
    --brand-blue-dark: #174b88;
    --text-dark: #2c2c2c;
    --text-grey: #6d6d6d;
    --paper: #ffffff;
    --backdrop: #ececec;
    --sky-top: #8fb9e0;
    --sky-low: #d9e6f1;
    --roof: #8d8f93;
    --panel-dark: #243f6e;
    --panel-light: #4f6f9e;
  }
  * { box-sizing: border-box; margin: 0; padding: 0; }
  html, body { width: 1200px; height: 1200px; overflow: hidden; }
  body {
    background: var(--backdrop);
    font-family: "Open Sans", Arial, sans-serif;
    color: var(--text-dark);
    position: relative;
  }
  .flyer {
    position: absolute;
    top: 140px;
    width: 430px;
    height: 920px;
    background: var(--paper);
    box-shadow: 0 6px 24px rgba(0,0,0,0.10);
    overflow: hidden;
  }
  .flyer--front { left: 140px; }
  .flyer--back { left: 630px; }

  .brand {
    display: flex;
    align-items: center;
    justify-content: center;
    gap: 12px;
  }
  .brand__dot {
    width: 30px; height: 30px;
    border-radius: 50%;
    background: var(--brand-blue);
  }
  .brand__name {
    font-weight: 700;
    color: var(--brand-blue);
    letter-spacing: 0.5px;
    font-size: 34px;
    text-transform: uppercase;
  }
  .flyer--front .brand { height: 200px; }
  .flyer--back .brand { margin-top: 56px; }
  .flyer--back .brand__name { font-size: 24px; }
  .flyer--back .brand__dot { width: 22px; height: 22px; }

  /* front */
  .hero {
    position: relative;
    height: 470px;
  }
  .hero__photo {
    position: absolute; inset: 0;
    background: linear-gradient(180deg, var(--sky-top) 0%, var(--sky-low) 28%, #a9acb1 40%, var(--roof) 70%, #6f7276 100%);
  }
  .hero__band {
    position: absolute;
    left: 60px; right: 0;
    bottom: 40px;
    height: 92px;
    background: rgba(31,95,168,0.9);
    display: flex;
    flex-direction: column;
    justify-content: center;
    align-items: flex-end;
    padding-right: 30px;
  }
  .hero__band::after {
    content: "";
    position: absolute;
    right: 14px; top: 0; bottom: 0;
    width: 4px;
    background: #fff;
  }
  .hero__band span {
    color: #fff;
    font-weight: 800;
    font-size: 16.5px;
    letter-spacing: 1.2px;
    text-transform: uppercase;
    line-height: 1.45;
    text-align: right;
  }
  .calc-cta {
    display: flex;
    justify-content: flex-end;
    align-items: center;
    gap: 18px;
    padding: 30px 30px 0;
  }
  .calc-cta__text {
    text-align: right;
    font-weight: 700;
    font-size: 20px;
    line-height: 1.3;
    color: var(--text-dark);
  }
  .contact {
    font-size: 10.5px;
    color: var(--text-grey);
    line-height: 1.85;
  }
  .flyer--front .contact {
    text-align: right;
    padding: 26px 30px 0;
  }

  /* back */
  .work-photo {
    height: 165px;
    background: linear-gradient(160deg, #b7c6d8 0%, var(--panel-light) 35%, var(--panel-dark) 100%);
  }
  .back-content { padding: 40px 40px 0 44px; }
  .back-title {
    color: var(--brand-blue);
    font-weight: 800;
    font-size: 23px;
    line-height: 1.3;
  }
  .back-lead {
    margin-top: 10px;
    color: var(--text-grey);
    font-size: 13px;
    line-height: 1.45;
  }
  .features { list-style: none; margin-top: 36px; }
  .feature {
    display: flex;
    gap: 16px;
    margin-bottom: 36px;
    padding-left: 14px;
  }
  .feature__icon {
    flex: none;
    width: 38px; height: 38px;
    border-radius: 50%;
    background: var(--brand-blue);
    display: flex; align-items: center; justify-content: center;
    margin-top: 6px;
  }
  .feature__title {
    font-weight: 700;
    font-size: 14px;
    color: var(--text-dark);
  }
  .feature__text {
    margin-top: 6px;
    font-size: 10.5px;
    color: var(--text-grey);
    line-height: 1.75;
  }
  .flyer--back .contact {
    text-align: center;
    margin-top: 40px;
    padding: 0 20px;
  }
</style>
</head>
<body>

<section class="flyer flyer--front">
  <div class="brand">
    <span class="brand__dot"></span>
    <span class="brand__name">Birkenhaintom</span>
  </div>

  <div class="hero">
    <div class="hero__photo" role="img" aria-label="Foto: Hausdach mit Ziegeln, Schornstein und montierten Solarmodulen vor blauem Himmel"></div>
    <div class="hero__band">
      <span>Senken Sie Ihre Stromkosten</span>
      <span>mit einer Photovoltaikanlage</span>
    </div>
  </div>

  <div class="calc-cta">
    <p class="calc-cta__text">Berechnen Sie jetzt<br>Ihre Gesamtkosten online!</p>
    <svg class="calc-cta__icon" width="36" height="44" viewBox="0 0 36 44" aria-hidden="true">
      <rect x="2" y="2" width="32" height="40" rx="2" fill="none" stroke="var(--brand-blue)" stroke-width="3"/>
      <rect x="8" y="8" width="20" height="9" fill="var(--brand-blue)"/>
      <rect x="8" y="23" width="5" height="4" fill="var(--brand-blue)"/>
      <rect x="16" y="23" width="5" height="4" fill="var(--brand-blue)"/>
      <rect x="24" y="23" width="4" height="11" fill="var(--brand-blue)"/>
      <rect x="8" y="30" width="5" height="4" fill="var(--brand-blue)"/>
      <rect x="16" y="30" width="5" height="4" fill="var(--brand-blue)"/>
    </svg>
  </div>

  <address class="contact" style="font-style:normal">
    Adresse: Lindenweg 14, 24103 Kiel, Deutschland<br>
    E-Mail: kontakt@birkenhaintom-beispiel.de &nbsp;|&nbsp; Web: www.birkenhaintom-beispiel.de<br>
    Telefon: +49 431 5550190 &nbsp;|&nbsp; +49 431 5550180
  </address>
</section>

<section class="flyer flyer--back">
  <div class="work-photo" role="img" aria-label="Foto: Monteur befestigt Solarmodule auf einem Dach"></div>

  <div class="back-content">
    <h2 class="back-title">Sie denken über eine<br>Photovoltaikanlage nach?</h2>
    <p class="back-lead">Nutzen Sie unseren Online-Rechner und lassen Sie sich von den Einsparungen überzeugen!</p>

    <ul class="features">
      <li class="feature">
        <span class="feature__icon">
          <svg width="20" height="20" viewBox="0 0 20 20" aria-hidden="true">
            <path d="M3 10 L10 3 L17 10 M5 8.5 V17 H15 V8.5" fill="none" stroke="#fff" stroke-width="1.8" stroke-linejoin="round"/>
          </svg>
        </span>
        <div>
          <h3 class="feature__title">Zuverlässigkeit</h3>
          <p class="feature__text">Vertrauen Sie auf unsere Zuverlässigkeit -<br>von der Beratung bis zur Installation Ihrer<br>Photovoltaikanlage.</p>
        </div>
      </li>
      <li class="feature">
        <span class="feature__icon">
          <svg width="20" height="20" viewBox="0 0 20 20" aria-hidden="true">
            <path d="M4 8 A6.5 6.5 0 0 1 16 7 M16 12 A6.5 6.5 0 0 1 4 13" fill="none" stroke="#fff" stroke-width="1.8"/>
            <path d="M16 3 V7 H12 M4 17 V13 H8" fill="none" stroke="#fff" stroke-width="1.8"/>
          </svg>
        </span>
        <div>
          <h3 class="feature__title">Effizienz</h3>
          <p class="feature__text">Unsere Photovoltaikanlagen:<br>Effizient und nachhaltig für Ihren Haushalt.</p>
        </div>
      </li>
      <li class="feature">
        <span class="feature__icon">
          <svg width="20" height="20" viewBox="0 0 20 20" aria-hidden="true">
            <path d="M7 3 V7 M13 3 V7 M5 7 H15 V10 A5 5 0 0 1 5 10 Z M10 15 V18" fill="none" stroke="#fff" stroke-width="1.8" stroke-linejoin="round"/>
          </svg>
        </span>
        <div>
          <h3 class="feature__title">Geld sparen</h3>
          <p class="feature__text">Machen Sie sich unabhängig von<br>Strompreissteigerungen.</p>
        </div>
      </li>
    </ul>
  </div>

  <div class="brand">
    <span class="brand__dot"></span>
    <span class="brand__name">Birkenhaintom</span>
  </div>

  <address class="contact" style="font-style:normal">
    Adresse: Lindenweg 14, 24103 Kiel, Deutschland<br>
    E-Mail: kontakt@birkenhaintom-beispiel.de &nbsp;|&nbsp; Web: www.birkenhaintom-beispiel.de<br>
    Telefon: +49 431 5550190 &nbsp;|&nbsp; +49 431 5550180
  </address>
</section>

</body>
</html>
```